A start-up named "Corvath Therapeutics" - needs a new PowerPoint design

We need a new PowerPoint Design for an early-stage start-up named "Corvath Therapeutics" seeking to disrupt the current approach towards drug discovery within aging disorders.

We would like to build on Corvath's legacy, the founder of the modern science of genetics, by employing a multidisciplinary approach, experimenting, and providing elderly patients the attention they deserve.

We have selected the suffix "therapeutics" intentionally as it stands for (a medicine) the treatment of disease; the science of healing. Alzheimer’s treatment is a huge, urgent, unmet need:
- Shift from a disease-management system to a preventive medicine system
- Focus on increasing the health span, not only the life span

Target Market(s)

Pharma/ Biotech Executives Medical Institutions Healthcare professionals (MDs, nurses, payors, pharmacists, etc.) Patients

Industry/Entity Type

Healthcare

Other font styles liked:
• Celias

Colors
0054AA
0677BA
7BADD7
CADEEF
E8F1F8
E54698
E96AAD
F1A4CE
F9D9EA
FCEFF6
A7469A
B969AE
D3A5CF
EDDBEB
F8F0F9
6B429C
8869AF
B7A5CE
E3DAEB
F3F0F8

Requirements
Must have
• - differentiate from other companies named after Corvath - differentiate from other Pharma/ Biotech companies
Nice to have
• simplicity/ minimalist logo vivid colors gradient 3D Life-Sciences inspired Simple geometry Balance
Should not have
• mascot/ emblem watermark logo animated ink style nature-inspired inventive typography artistic chaos

```html
<!DOCTYPE html>
<html lang="en">
<head>
<meta charset="utf-8">
<title>Corvath Therapeutics – Presentation Slides</title>
<link rel="stylesheet" href="https://fonts.googleapis.com/css2?family=Montserrat:wght@400;500;600&display=swap">
<style>
:root{
  --black:#000;
  --ink:#ffffff;
  --blue:#12a6ec;
  --blue-deep:#1f7fd6;
  --indigo:#3b45b5;
  --purple:#6d1d8c;
  --violet:#7b2aa6;
  --muted:#8a8a96;
  --rule:#3a3a44;
  --track:#26262e;
  --glow:rgba(214,150,220,.35);
  --font:"Montserrat", sans-serif;
}
*{box-sizing:border-box;margin:0;padding:0}
html,body{width:1200px;height:3369px;overflow:hidden;background:#fff;font-family:var(--font)}
.slide{position:absolute;left:49px;width:1100px;height:618px;background:var(--black);overflow:hidden;box-shadow:0 0 22px var(--glow);color:var(--ink)}
.s1{top:47px}.s2{top:703px}.s3{top:1358px}.s4{top:2014px}.s5{top:2669px}
.art{position:absolute;inset:0;width:1100px;height:618px}
.brand{position:absolute;display:flex;align-items:center;gap:10px;font-weight:500;line-height:1}
.brand .mark{width:14px;height:14px;background:currentColor}
.brand .name{display:block;font-size:28px}
.brand .sub{display:block;font-size:12px;letter-spacing:2.4px;margin-top:3px}
.brand.lg .name{font-size:38px}.brand.lg .sub{font-size:16px;letter-spacing:3px}
.brand.blue{color:#3d7fe0}.brand.white{color:var(--ink)}
.grad-text{background:linear-gradient(90deg,#2f52c4,#7a2aa6);-webkit-background-clip:text;background-clip:text;color:transparent}
.h1{position:absolute;font-weight:500;font-size:40px;line-height:54px;white-space:nowrap}
.body{position:absolute;font-size:11px;line-height:17px;color:var(--ink)}
.sub-h{position:absolute;font-size:14px;font-weight:500;white-space:nowrap}
.bullets{position:absolute;list-style:none;font-size:10px;line-height:13px;width:390px}
.bullets li{position:relative;padding-left:14px;margin-bottom:13px}
.bullets li::before{content:"";position:absolute;left:0;top:2px;border-left:6px solid var(--violet);border-top:4px solid transparent;border-bottom:4px solid transparent}
.bullets.white li::before{border-left-color:var(--ink)}
.footer{position:absolute;left:38px;top:594px;font-size:10px;color:var(--violet);white-space:nowrap}
.footer .sep{margin:0 14px}
.stat{position:absolute;width:100px;height:100px}
.stat span{position:absolute;inset:0;display:flex;align-items:center;justify-content:center;font-size:21px;font-weight:500}
.contact{position:absolute;font-size:11px;line-height:21px;color:var(--violet);white-space:nowrap}
</style>
</head>
<body>

<!-- Slide 1: title -->
<section class="slide s1">
  <svg class="art" viewBox="0 0 1100 618">
    <defs>
      <linearGradient id="g1" x1="0" x2="1" y1="0" y2="0"><stop offset="0" stop-color="#12a6ec"/><stop offset=".45" stop-color="#3b45b5"/><stop offset="1" stop-color="#6d1d8c"/></linearGradient>
      <linearGradient id="p1" x1="0" x2="1" y1="0" y2="1"><stop offset="0" stop-color="#f2f6fb"/><stop offset=".5" stop-color="#9cc4e6"/><stop offset="1" stop-color="#3f7fc4"/></linearGradient>
    </defs>
    <polygon points="389,0 1100,0 1100,618 860,618 620,300" fill="url(#g1)"/>
    <polygon points="389,0 465,0 640,282 600,300" fill="#12a6ec"/>
    <polygon role="img" aria-label="Photo of a lab scientist in cap and goggles looking into a microscope" points="465,30 1062,30 1062,539 914,539 874,618 571,618 637,282" fill="url(#p1)"/>
    <polygon points="874,579 1100,579 1100,618 861,618" fill="#12a6ec"/>
    <line x1="373" y1="600" x2="870" y2="600" stroke="#3a3a44" stroke-width="1"/>
  </svg>
  <div class="brand blue lg" style="left:38px;top:42px"><i class="mark"></i><div><span class="name">Corvath</span><span class="sub">Therapeutics</span></div></div>
  <h1 class="h1 grad-text" style="left:38px;top:250px;white-space:normal;width:420px">Neque porro quisquam est qui</h1>
  <p class="h1" style="left:38px;top:385px">dolorem ipsum</p>
  <p class="footer">www.CorvathTherapeutics.com<span class="sep">|</span>+1 503 555 0148</p>
</section>

<!-- Slide 2: content with image -->
<section class="slide s2">
  <svg class="art" viewBox="0 0 1100 618">
    <defs>
      <linearGradient id="g2" x1="0" x2="1"><stop offset="0" stop-color="#1f8fe6"/><stop offset="1" stop-color="#6d1d8c"/></linearGradient>
      <radialGradient id="p2" cx=".5" cy=".45" r=".7"><stop offset="0" stop-color="#f4e3f2"/><stop offset=".45" stop-color="#8fd0ef"/><stop offset="1" stop-color="#3aa3d8"/></radialGradient>
    </defs>
    <rect x="853" y="0" width="247" height="618" fill="url(#g2)"/>
    <rect x="815" y="42" width="38" height="576" fill="#12a6ec"/>
    <rect role="img" aria-label="Illustration of blue and pink chromosomes over a DNA helix" x="485" y="100" width="537" height="417" fill="url(#p2)"/>
    <line x1="373" y1="600" x2="1100" y2="600" stroke="#3a3a44"/>
  </svg>
  <div class="brand white" style="left:36px;top:28px"><i class="mark"></i><div><span class="name">Corvath</span><span class="sub">Therapeutics</span></div></div>
  <h2 class="h1" style="left:38px;top:92px;white-space:normal;width:440px">Neque porro quisquam est qui</h2>
  <p class="body" style="left:38px;top:220px;width:395px">Sed ut perspiciatis unde omnis iste natus error sit voluptatem accusantium doloremque laudantium, totam rem aperiam, eaque ipsa quae ab illo inventore veritatis et quasi architecto beatae vitae dicta sunt explicabo.</p>
  <h3 class="sub-h" style="left:38px;top:305px">Nemo enim ipsam voluptatem quia voluptas</h3>
  <ul class="bullets" style="left:38px;top:340px">
    <li>Sed ut perspiciatis unde omnis iste natus error sit voluptatem</li>
    <li>Doloremque laudantium, totam rem aperiam, eaque ipsa quae ab illo inventore veritatis et quasi architecto</li>
    <li>Beatae vitae dicta sunt explicabo.</li>
    <li>Sed ut perspiciatis unde omnis iste natus error sit voluptatem</li>
    <li>Doloremque laudantium, totam rem aperiam, eaque ipsa quae ab illo inventore veritatis et quasi architecto</li>
    <li>Beatae vitae dicta sunt explicabo.</li>
  </ul>
  <p class="footer">www.CorvathTherapeutics.com<span class="sep">|</span>+1 503 555 0148</p>
</section>

<!-- Slide 3: text right, image left -->
<section class="slide s3">
  <svg class="art" viewBox="0 0 1100 618">
    <defs>
      <radialGradient id="p3" cx=".55" cy=".4" r=".8"><stop offset="0" stop-color="#ff3d6e"/><stop offset=".45" stop-color="#8a2a6a"/><stop offset="1" stop-color="#2a2350"/></radialGradient>
    </defs>
    <polygon points="700,77 752,77 345,541 290,541" fill="#6d1d8c"/>
    <polygon points="0,0 709,0 300,541 0,541" fill="#12a6ec"/>
    <polygon role="img" aria-label="Photo of a glowing red DNA double helix on a dark bokeh background" points="38,31 634,31 235,541 38,541" fill="url(#p3)"/>
    <polygon points="0,541 345,541 365,581 0,581" fill="#6d1d8c"/>
    <polygon points="0,581 380,581 400,618 0,618" fill="#12a6ec"/>
    <line x1="400" y1="600" x2="1060" y2="600" stroke="#3a3a44"/>
  </svg>
  <div class="brand blue" style="left:915px;top:30px"><i class="mark"></i><div><span class="name">Corvath</span><span class="sub">Therapeutics</span></div></div>
  <h2 class="h1" style="right:58px;top:160px;text-align:right;color:var(--blue)">Quisquam est qui</h2>
  <p class="h1" style="right:58px;top:214px;text-align:right">dolorem ipsum</p>
  <p class="body" style="left:575px;top:287px;width:469px;text-align:justify;text-align-last:right;line-height:20.7px;font-size:10.5px">Sed ut perspiciatis unde omnis iste natus error sit voluptatem accusantium doloremque laudantium, totam rem aperiam, eaque ipsa quae ab illo inventore veritatis et quasi architecto beatae vitae dicta sunt explicabo. Nemo enim ipsam voluptatem quia voluptas sit aspernatur aut odit aut fugit, sed quia consequuntur magni dolores eos qui ratione voluptatem sequi nesciunt. Neque porro quisquam est, qui dolorem ipsum quia dolor sit amet, consectetur, adipisci velit, sed quia non numquam eius modi tempora incidunt ut labore et dolore.</p>
  <p class="body" style="left:575px;top:452px;width:469px;text-align:justify;text-align-last:right;line-height:20.7px;font-size:10.5px">Ut enim ad minima veniam, quis nostrum exercitationem ullam corporis suscipit laboriosam, nisi ut aliquid ex ea commodi consequatur? Quis autem vel eum iure reprehenderit qui in ea voluptate velit esse quam nihil molestiae consequatur, vel illum qui dolorem eum fugiat quo voluptas nulla pariatur?</p>
  <p class="footer" style="color:#4a2a9a">www.CorvathTherapeutics.com<span class="sep">|</span>+1 503 555 0148</p>
</section>

<!-- Slide 4: statistics -->
<section class="slide s4">
  <svg class="art" viewBox="0 0 1100 618">
    <defs>
      <linearGradient id="g4" x1="0" x2="1"><stop offset="0" stop-color="#1f8fe6"/><stop offset="1" stop-color="#6d1d8c"/></linearGradient>
      <radialGradient id="p4" cx=".5" cy=".5" r=".7"><stop offset="0" stop-color="#2a3a8c"/><stop offset="1" stop-color="#1a2466"/></radialGradient>
    </defs>
    <rect x="853" y="0" width="247" height="618" fill="url(#g4)"/>
    <rect x="815" y="42" width="38" height="576" fill="#12a6ec"/>
    <rect role="img" aria-label="Photo of assorted colourful pills and capsules on a navy surface" x="485" y="101" width="537" height="414" fill="url(#p4)"/>
    <line x1="373" y1="600" x2="1100" y2="600" stroke="#3a3a44"/>
  </svg>
  <div class="brand white" style="left:36px;top:28px"><i class="mark"></i><div><span class="name">Corvath</span><span class="sub">Therapeutics</span></div></div>
  <h2 class="h1" style="left:38px;top:92px;white-space:normal;width:440px">Neque porro quisquam est qui</h2>
  <p class="body" style="left:38px;top:222px;width:395px">Sed ut perspiciatis unde omnis iste natus error sit voluptatem accusantium doloremque laudantium, totam rem aperiam</p>
  <h3 class="sub-h" style="left:38px;top:271px">Nemo enim ipsam voluptatem quia voluptas</h3>
  <ul class="bullets white" style="left:38px;top:305px">
    <li>Sed ut perspiciatis unde omnis iste natus error sit voluptatem</li>
    <li>Doloremque laudantium, totam rem aperiam, eaque ipsa quae ab illo inventore veritatis et quasi architecto</li>
  </ul>
  <div class="stat" style="left:38px;top:400px">
    <svg viewBox="0 0 100 100" width="100" height="100"><circle cx="50" cy="50" r="45" fill="none" stroke="var(--track)" stroke-width="7"/><circle cx="50" cy="50" r="45" fill="none" stroke="#4b2a8c" stroke-width="7" stroke-dasharray="183.8 282.7" transform="rotate(-90 50 50)"/></svg>
    <span style="color:#5a2f9e">65%</span>
  </div>
  <div class="stat" style="left:177px;top:400px">
    <svg viewBox="0 0 100 100" width="100" height="100"><circle cx="50" cy="50" r="45" fill="none" stroke="var(--track)" stroke-width="7"/><circle cx="50" cy="50" r="45" fill="none" stroke="var(--blue)" stroke-width="7" stroke-dasharray="240.3 282.7" transform="rotate(-90 50 50)"/></svg>
    <span style="color:var(--blue)">85%</span>
  </div>
  <div class="stat" style="left:315px;top:400px">
    <svg viewBox="0 0 100 100" width="100" height="100"><circle cx="50" cy="50" r="45" fill="none" stroke="var(--track)" stroke-width="7"/><circle cx="50" cy="50" r="45" fill="none" stroke="var(--purple)" stroke-width="7" stroke-dasharray="268.6 282.7" transform="rotate(-90 50 50)"/></svg>
    <span style="color:#8a2aa6">95%</span>
  </div>
  <p class="footer">www.CorvathTherapeutics.com<span class="sep">|</span>+1 503 555 0148</p>
</section>

<!-- Slide 5: thank you / contact -->
<section class="slide s5">
  <svg class="art" viewBox="0 0 1100 618">
    <defs>
      <linearGradient id="g5" x1="0" x2="1"><stop offset="0" stop-color="#1f8fe6"/><stop offset="1" stop-color="#6d1d8c"/></linearGradient>
      <linearGradient id="p5" x1="0" x2="1" y1="0" y2="1"><stop offset="0" stop-color="#eef4fb"/><stop offset=".5" stop-color="#7fb2de"/><stop offset="1" stop-color="#2a3f7a"/></linearGradient>
    </defs>
    <rect x="0" y="0" width="255" height="618" fill="url(#g5)"/>
    <rect x="255" y="42" width="37" height="576" fill="#12a6ec"/>
    <rect role="img" aria-label="Photo of a gloved hand holding a petri dish with a pipette over a well plate" x="80" y="100" width="538" height="417" fill="url(#p5)"/>
    <line x1="292" y1="603" x2="1100" y2="603" stroke="#3a3a44"/>
    <g fill="none" stroke="#6d1d8c" stroke-width="1.6">
      <circle cx="662" cy="366" r="17"/>
      <path d="M656 358c-1 4 2 10 6 13 2 1 4 2 6 1l1-3-3-2-2 1c-2-1-4-3-5-5l1-2-2-3z"/>
      <circle cx="862" cy="366" r="17"/>
      <rect x="854" y="360" width="16" height="12" rx="1.5"/>
      <path d="M854 361l8 6 8-6"/>
      <circle cx="662" cy="443" r="17"/>
      <path d="M662 453c-5-6-7-9-7-12a7 7 0 0 1 14 0c0 3-2 6-7 12z"/>
      <circle cx="662" cy="441" r="2.2"/>
    </g>
  </svg>
  <div class="brand blue" style="left:911px;top:28px"><i class="mark"></i><div><span class="name">Corvath</span><span class="sub">Therapeutics</span></div></div>
  <h2 class="h1 grad-text" style="left:645px;top:140px;line-height:53px">Thank You!<br>quisquam est qui</h2>
  <p class="body" style="left:645px;top:283px;width:390px">Sed ut perspiciatis unde omnis iste natus error sit voluptatem accusantium doloremque laudantium, totam rem aperiam</p>
  <p class="contact" style="left:697px;top:351px">Phone:<br>+1 503 555 0148</p>
  <p class="contact" style="left:898px;top:351px">Email:<br>hello@corvath.com</p>
  <p class="contact" style="left:697px;top:428px">1180 Harbor Ridge Ave<br>Suite 300 Alder Bay, OR 97000</p>
</section>

</body>
</html>
```